Powerpoint contest

We need to re-design our powerpoints to be much more consistent. All the details are mentioned here. I have more than 30 slides to be created in all.

https://www.pagevault.example/gravik/All-Powerpoints-3c7e91d2ab0f4e6c8d15b27a90e4cf61

Requirements
Must have
• Colors should be greyscale and bravocell pink (ea0a8e) used in small amounts just for accents.

```html
<!DOCTYPE html>
<html lang="en">
<head>
<meta charset="utf-8">
<title>Veltrix webinar deck</title>
<link href="https://fonts.googleapis.com/css2?family=Domine:wght@400;700&family=Nunito:wght@300;400;700;800;900&display=swap" rel="stylesheet">
<style>
:root{
  --pink:#ea0a8e;
  --ink:#1b1b1b;
  --grey:#8a8a8a;
  --light:#e3e3e3;
  --panel:#efefef;
  --board:#a5a5a5;
  --dark:#1e1e1e;
  --white:#ffffff;
}
*{box-sizing:border-box;margin:0;padding:0}
html,body{width:1200px;height:5324px;overflow:hidden;background:var(--board)}
body{position:relative;font-family:'Nunito',sans-serif;color:var(--ink)}
.slide{position:absolute;left:37px;width:1126px;height:632px;background:var(--white);overflow:hidden}
.abs{position:absolute}
.serif{font-family:'Domine',serif;font-weight:700}
.brand{position:absolute;display:flex;align-items:center;gap:8px;font-family:'Nunito',sans-serif;font-weight:800;color:var(--ink)}
.brand .mark{border-radius:50%;background:var(--pink)}
.deco{position:absolute}
.footer-line{position:absolute;left:0;right:0;top:587px;height:2px;background:#f0f0f0}
.footer-line::after{content:"";position:absolute;left:533px;width:46px;top:-1px;height:3px;background:var(--pink)}
.footer-brand{left:58px;top:596px;font-size:21px}
.footer-brand .mark{width:14px;height:14px}
.page-num{position:absolute;right:0;bottom:0;width:90px;height:90px}
.center{text-align:center}
.pct sup{font-size:.45em;color:var(--pink);font-family:'Nunito',sans-serif;font-weight:400;vertical-align:.9em;margin-left:2px}
.ring-label{font-size:15px;line-height:18px;color:#444;text-align:center}
.qa-letter{position:absolute;line-height:1;font-weight:800;white-space:nowrap}
</style>
</head>
<body>

<section class="slide" style="top:54px">
  <div class="deco" role="img" aria-label="Curving field of grey and pink dots" style="left:0;top:0;width:355px;height:632px;background:radial-gradient(ellipse at 60% 40%,#e2e2e2 0%,#f1f1f1 45%,#ffffff 75%)"></div>
  <h1 class="abs" style="left:434px;top:180px;font-size:52px;color:var(--pink);font-weight:400;font-family:'Domine',serif">Title of the webinar</h1>
  <p class="abs" style="left:434px;top:292px;font-size:27px;font-weight:700">Subtitle here</p>
  <p class="abs" style="left:434px;top:366px;font-size:18px">Presenter 1 | Presenter 2</p>
  <p class="abs" style="left:434px;top:428px;font-size:14px;color:#aaa">Date here</p>
  <div class="abs" style="left:434px;right:0;top:483px;height:2px;background:#f0f0f0"></div>
  <div class="abs" style="left:784px;width:46px;top:482px;height:3px;background:var(--pink)"></div>
  <div class="brand" style="left:439px;top:516px;font-size:70px;gap:18px"><span class="mark" style="width:40px;height:40px"></span>Veltrix</div>
</section>

<section class="slide" style="top:710px">
  <h2 class="abs center" style="left:0;right:0;top:176px;font-size:62px;font-weight:300">Thank you</h2>
  <div class="abs" style="left:542px;width:42px;top:282px;height:3px;background:var(--pink)"></div>
  <div class="brand" style="left:476px;top:334px;font-size:28px"><span class="mark" style="width:18px;height:18px"></span>Veltrix</div>
  <div class="deco" role="img" aria-label="Perspective floor of grey dots with scattered pink dots" style="left:0;right:0;top:435px;bottom:0;background:linear-gradient(#ffffff,#ececec)"></div>
</section>

<section class="slide" style="top:1363px;background:var(--dark)">
  <div class="qa-letter" style="left:232px;top:170px;font-size:260px;color:var(--pink)">Q</div>
  <div class="qa-letter" style="left:440px;top:262px;font-size:110px;color:var(--pink)">&amp;</div>
  <div class="qa-letter" style="left:530px;top:170px;font-size:260px;color:var(--white)">A</div>
  <div class="deco" role="img" aria-label="Speech bubble illustration with a question mark" style="left:790px;top:268px;width:310px;height:364px;border-radius:50% 50% 0 0;background:radial-gradient(circle at 50% 42%,#3a3a3a 0%,#2a2a2a 55%,#1e1e1e 80%)"></div>
</section>

<section class="slide" style="top:2020px">
  <div class="abs" style="left:0;top:198px;width:818px;bottom:0;background:var(--panel)"></div>
  <div class="abs" style="left:772px;width:46px;top:196px;height:3px;background:var(--pink)"></div>
  <div class="deco" role="img" aria-label="Small curving cluster of grey and pink dots" style="left:940px;top:4px;width:180px;height:230px;background:radial-gradient(ellipse at 50% 50%,#e0e0e0 0%,#f3f3f3 50%,#ffffff 75%)"></div>
  <h2 class="abs serif" style="left:58px;top:260px;font-size:56px;font-weight:400">Section divider title</h2>
  <p class="abs" style="left:58px;top:456px;font-size:26px;color:var(--grey)">subtitle</p>
  <div class="brand footer-brand"><span class="mark"></span>Veltrix</div>
</section>

<section class="slide" style="top:2676px">
  <h2 class="abs center serif" style="left:0;right:0;top:180px;font-size:38px;font-weight:400">Our company</h2>
  <p class="abs center" style="left:165px;width:796px;top:244px;font-size:16.5px;line-height:29.5px;color:#333">Veltrix is an international software company that has pioneered the Corvane application life cycle development sector. Our firm is focused on transforming the DevOps experience for our clients, allowing them to accelerate their operational agility and improve collaboration. The unique architecture of our products provides security, governance and compliance abilities that are unparalleled in the industry. We are trusted by some of the largest brands around the world and provide customized assistance, training and knowledge transfer to each of our customers who operate in a multitude of industries</p>
  <div class="footer-line"></div>
  <div class="brand footer-brand"><span class="mark"></span>Veltrix</div>
  <svg class="page-num" viewBox="0 0 90 90"><circle cx="90" cy="90" r="64" fill="none" stroke="var(--pink)" stroke-width="2" stroke-dasharray="2 4"/><circle cx="90" cy="90" r="46" fill="#e6e6e6"/><text x="60" y="72" font-family="Nunito,sans-serif" font-size="11" fill="#555">6</text></svg>
</section>

<section class="slide" style="top:3331px">
  <h2 class="abs serif" style="left:58px;top:224px;font-size:38px;font-weight:400">Financial strength</h2>
  <p class="abs" style="left:58px;top:292px;width:360px;font-size:16.5px;line-height:29px;color:#333">Veltrix has demonstrated incredible growth and been cash flow positive since inception in 2014. It is completely funded by customer revenue.</p>
  <svg class="abs" style="left:610px;top:130px" width="350" height="350" viewBox="0 0 350 350">
    <circle cx="175" cy="175" r="168" fill="none" stroke="var(--light)" stroke-width="3"/>
    <circle cx="175" cy="175" r="168" fill="none" stroke="var(--pink)" stroke-width="4" pathLength="100" stroke-dasharray="92 8" transform="rotate(-90 175 175)"/>
  </svg>
  <div class="abs center pct serif" style="left:610px;width:350px;top:196px;font-size:124px;line-height:1">92<sup>%</sup></div>
  <p class="abs center" style="left:610px;width:350px;top:330px;font-size:16px;line-height:22px;color:#333">of earnings are re-invested<br>back into the company</p>
  <div class="deco" role="img" aria-label="Stack of coins icon" style="left:768px;top:394px;width:36px;height:36px;border-radius:6px;background:#d6d6d6"></div>
  <div class="footer-line"></div>
  <div class="brand footer-brand"><span class="mark"></span>Veltrix</div>
  <svg class="page-num" viewBox="0 0 90 90"><circle cx="90" cy="90" r="64" fill="none" stroke="var(--pink)" stroke-width="2" stroke-dasharray="2 4"/><circle cx="90" cy="90" r="46" fill="#e6e6e6"/><text x="60" y="72" font-family="Nunito,sans-serif" font-size="11" fill="#555">7</text></svg>
</section>

<section class="slide" style="top:3986px">
  <h2 class="abs serif" style="left:58px;top:38px;font-size:38px;font-weight:400">Revenue investments</h2>
  <svg class="abs" style="left:0;top:190px" width="1126" height="240" viewBox="0 0 1126 240">
    <g fill="none" stroke-width="3">
      <circle cx="169" cy="120" r="112" stroke="var(--light)"/>
      <circle cx="169" cy="120" r="112" stroke="var(--pink)" pathLength="100" stroke-dasharray="35 65" transform="rotate(-90 169 120)"/>
      <circle cx="431" cy="120" r="112" stroke="var(--light)"/>
      <circle cx="431" cy="120" r="112" stroke="var(--pink)" pathLength="100" stroke-dasharray="28 72" transform="rotate(-90 431 120)"/>
      <circle cx="694" cy="120" r="112" stroke="var(--light)"/>
      <circle cx="694" cy="120" r="112" stroke="var(--pink)" pathLength="100" stroke-dasharray="14 86" transform="rotate(-90 694 120)"/>
      <circle cx="956" cy="120" r="112" stroke="var(--light)"/>
      <circle cx="956" cy="120" r="112" stroke="var(--pink)" pathLength="100" stroke-dasharray="16 84" transform="rotate(-90 956 120)"/>
    </g>
  </svg>
  <div class="abs center pct serif" style="left:57px;width:224px;top:252px;font-size:76px;line-height:1">35<sup>%</sup></div>
  <div class="abs center pct serif" style="left:319px;width:224px;top:252px;font-size:76px;line-height:1">28<sup>%</sup></div>
  <div class="abs center pct serif" style="left:582px;width:224px;top:252px;font-size:76px;line-height:1">14<sup>%</sup></div>
  <div class="abs center pct serif" style="left:844px;width:224px;top:252px;font-size:76px;line-height:1">16<sup>%</sup></div>
  <p class="abs ring-label" style="left:57px;width:224px;top:343px">Sales &amp;<br>Marketing</p>
  <p class="abs ring-label" style="left:319px;width:224px;top:343px">Research &amp;<br>Development</p>
  <p class="abs ring-label" style="left:582px;width:224px;top:343px">Customer<br>Support</p>
  <p class="abs ring-label" style="left:844px;width:224px;top:343px">Retained<br>Earnings</p>
  <div class="footer-line"></div>
  <div class="brand footer-brand"><span class="mark"></span>Veltrix</div>
  <svg class="page-num" viewBox="0 0 90 90"><circle cx="90" cy="90" r="64" fill="none" stroke="var(--pink)" stroke-width="2" stroke-dasharray="2 4"/><circle cx="90" cy="90" r="46" fill="#e6e6e6"/><text x="60" y="72" font-family="Nunito,sans-serif" font-size="11" fill="#555">8</text></svg>
</section>

<section class="slide" style="top:4640px">
  <h2 class="abs serif" style="left:58px;top:38px;font-size:38px;font-weight:400">Customer satisfaction</h2>
  <div class="abs" style="left:537px;top:182px;width:1px;height:372px;background:var(--light)"></div>
  <div class="abs center pct serif" style="left:97px;width:400px;top:196px;font-size:80px;line-height:1">103<sup>%</sup></div>
  <p class="abs center" style="left:97px;width:400px;top:280px;font-size:15px;color:#444">Revenue retention</p>
  <div class="deco" role="img" aria-label="Illustration of a briefcase and money bag with a pink upward arrow" style="left:200px;top:335px;width:196px;height:176px;background:linear-gradient(135deg,#f6c6e2,#d9d9d9 60%,#bdbdbd)"></div>
  <div class="abs center pct serif" style="left:607px;width:400px;top:196px;font-size:80px;line-height:1">98.2<sup>%</sup></div>
  <p class="abs center" style="left:607px;width:400px;top:280px;font-size:15px;color:#444">Customers would recommend Veltrix</p>
  <div class="deco" role="img" aria-label="Grid of grey people figures with a pink thumbs-up badge" style="left:665px;top:356px;width:283px;height:128px;background:radial-gradient(circle at 50% 50%,var(--pink) 0 44px,#e4e4e4 46px,#efefef 100%)"></div>
  <div class="footer-line"></div>
  <div class="brand footer-brand"><span class="mark"></span>Veltrix</div>
  <svg class="page-num" viewBox="0 0 90 90"><circle cx="90" cy="90" r="64" fill="none" stroke="var(--pink)" stroke-width="2" stroke-dasharray="2 4"/><circle cx="90" cy="90" r="46" fill="#e6e6e6"/><text x="60" y="72" font-family="Nunito,sans-serif" font-size="11" fill="#555">9</text></svg>
</section>

</body>
</html>
```